Bref créative
Dormly Nest
HMO Specialists
Professional
Rafik Toumi
Partner
We dont want an adress on the business card
Rafik@dormlynest.co.uk
www.dormlynest.co.uk
I Would like to try with HMO Specialists...O
Or
Letting Agency
Or nothing in the subtitle
The Logo

```html
<!DOCTYPE html>
<html lang="en">
<head>
<meta charset="utf-8">
<title>Dormly Nest Stationery</title>
<link href="https://fonts.googleapis.com/css2?family=Open+Sans:wght@400;600;700&display=swap" rel="stylesheet">
<style>
:root{
  --backdrop:#3b3c3e;
  --paper:#ffffff;
  --ink:#33414c;
  --brand:#2b5f74;
  --blue:#1b84c6;
  --navy:#0f4d7c;
  --green:#3f9b31;
  --lime:#8cc63f;
  --label:#d9d9d9;
}
*{box-sizing:border-box;margin:0;padding:0}
html,body{width:1200px;height:743px;overflow:hidden;background:var(--backdrop);font-family:"Open Sans",sans-serif;color:var(--ink)}
.canvas{position:relative;width:1200px;height:743px}
.item{position:absolute;background:var(--paper);box-shadow:0 4px 10px rgba(0,0,0,.45);overflow:hidden}
.item svg.wave{position:absolute;inset:0;width:100%;height:100%}
.label{position:absolute;font-size:6px;color:var(--label);white-space:nowrap}
.brand{position:absolute;display:flex;align-items:center;gap:4px;font-weight:700;color:var(--brand);letter-spacing:.5px;text-transform:uppercase;white-space:nowrap}
.brand .mark{background:var(--brand);display:block}
.contact{position:absolute;font-size:4.5px;line-height:1.55;color:var(--ink);white-space:nowrap}
.contact b{font-weight:700;font-size:5.5px}
.card{width:144px;height:77px}
.card .brand{font-size:10px}
.card .brand .mark{width:8px;height:8px}
.card--dark{background:linear-gradient(135deg,#2c3238,#4a5560)}
.card--green{background:linear-gradient(135deg,var(--lime),var(--green))}
.card--dark .brand,.card--green .brand{color:#fff}
.card--dark .brand .mark,.card--green .brand .mark{background:#fff}
.envelope{width:480px}
.envelope .brand{font-size:14px}
.envelope .brand .mark{width:11px;height:11px}
.letterhead{width:322px;height:463px}
.letterhead .brand{font-size:15px;top:26px;left:22px}
.letterhead .brand .mark{width:12px;height:12px}
.footer-line{position:absolute;bottom:8px;left:0;right:0;text-align:center;font-size:4px;color:var(--ink)}
.back{width:480px}
</style>
</head>
<body>
<main class="canvas">

  <!-- business cards, top row -->
  <span class="label" style="left:268px;top:33px">Business Card Front | Option 1</span>
  <span class="label" style="left:420px;top:33px">Business Card Front | Option 2</span>
  <span class="label" style="left:572px;top:33px">Business Card Front | Option 3</span>

  <section class="item card" style="left:252px;top:43px">
    <svg class="wave" viewBox="0 0 100 100" preserveAspectRatio="none">
      <path d="M62,0 C78,30 84,70 100,100 L100,0Z" fill="var(--green)"/>
      <path d="M70,0 C84,32 88,72 100,98 L100,0Z" fill="var(--paper)"/>
      <path d="M74,0 C87,34 90,74 100,96 L100,0Z" fill="var(--blue)"/>
    </svg>
    <div class="brand" style="left:8px;top:8px"><i class="mark"></i>Dormly Nest</div>
    <div class="contact" style="left:48px;top:24px"><b>Rafik Toumi</b><br>Partner</div>
    <div class="contact" style="left:8px;top:46px">M 07700 900123<br>Rafik@dormlynest.co.uk<br>www.dormlynest.co.uk</div>
  </section>

  <section class="item card" style="left:408px;top:43px">
    <svg class="wave" viewBox="0 0 100 100" preserveAspectRatio="none">
      <path d="M0,100 C40,80 70,70 100,40 L100,100Z" fill="var(--navy)"/>
      <path d="M0,100 C45,86 72,78 100,52 L100,100Z" fill="var(--blue)"/>
    </svg>
    <div class="brand" style="left:8px;top:8px"><i class="mark"></i>Dormly Nest</div>
    <div class="contact" style="left:48px;top:24px"><b>Rafik Toumi</b><br>Partner</div>
    <div class="contact" style="left:8px;top:40px">M 07700 900123<br>Rafik@dormlynest.co.uk<br>www.dormlynest.co.uk</div>
  </section>

  <section class="item card" style="left:557px;top:43px">
    <svg class="wave" viewBox="0 0 100 100" preserveAspectRatio="none">
      <path d="M0,100 C40,70 70,60 100,20 L100,100Z" fill="var(--green)"/>
      <path d="M0,100 C45,80 72,72 100,38 L100,100Z" fill="var(--paper)"/>
      <path d="M0,100 C50,86 75,80 100,50 L100,100Z" fill="var(--blue)"/>
    </svg>
    <div class="brand" style="left:8px;top:8px"><i class="mark"></i>Dormly Nest</div>
    <div class="contact" style="left:82px;top:24px"><b>Rafik Toumi</b><br>Partner</div>
    <div class="contact" style="left:8px;top:34px">M 07700 900123<br>Rafik@dormlynest.co.uk<br>www.dormlynest.co.uk</div>
  </section>

  <!-- business cards, back row -->
  <span class="label" style="left:268px;top:128px">Business Card Back | Option 1</span>
  <span class="label" style="left:420px;top:128px">Business Card Back | Option 2</span>
  <span class="label" style="left:572px;top:128px">Business Card Back | Option 3</span>

  <section class="item card" style="left:252px;top:138px">
    <div class="brand" style="left:32px;top:32px"><i class="mark"></i>Dormly Nest</div>
  </section>
  <section class="item card card--dark" style="left:408px;top:138px">
    <div class="brand" style="left:32px;top:32px"><i class="mark"></i>Dormly Nest</div>
  </section>
  <section class="item card card--green" style="left:557px;top:138px">
    <div class="brand" style="left:32px;top:32px"><i class="mark"></i>Dormly Nest</div>
  </section>

  <!-- envelope fronts -->
  <span class="label" style="left:900px;top:19px">Envelope Front | Option 1</span>
  <section class="item envelope" style="left:713px;top:29px;height:180px">
    <svg class="wave" viewBox="0 0 100 100" preserveAspectRatio="none">
      <path d="M68,0 C85,25 92,55 100,70 L100,0Z" fill="var(--green)"/>
      <path d="M74,0 C88,24 94,50 100,60 L100,0Z" fill="var(--paper)"/>
      <path d="M60,100 C80,85 92,70 100,55 L100,100Z" fill="var(--blue)"/>
      <path d="M66,100 C84,90 94,78 100,68 L100,100Z" fill="var(--paper)"/>
      <path d="M72,100 C88,93 96,84 100,78 L100,100Z" fill="var(--navy)"/>
    </svg>
    <div class="brand" style="left:14px;top:14px"><i class="mark"></i>Dormly Nest</div>
    <div class="contact" style="left:30px;top:38px">Dormly Nest Ltd<br>12 Park Row<br>Leeds LS1 5HD<br>www.dormlynest.co.uk</div>
  </section>

  <span class="label" style="left:900px;top:207px">Envelope Front | Option 2</span>
  <section class="item envelope" style="left:713px;top:216px;height:180px">
    <svg class="wave" viewBox="0 0 100 100" preserveAspectRatio="none">
      <path d="M0,100 C30,70 65,72 100,40 L100,100Z" fill="var(--green)"/>
      <path d="M0,100 C35,78 68,80 100,52 L100,100Z" fill="var(--paper)"/>
      <path d="M0,100 C40,84 70,86 100,60 L100,100Z" fill="var(--blue)"/>
    </svg>
    <div class="brand" style="left:14px;top:14px"><i class="mark"></i>Dormly Nest</div>
    <div class="contact" style="left:30px;top:38px">Dormly Nest Ltd<br>12 Park Row<br>Leeds LS1 5HD<br>www.dormlynest.co.uk</div>
  </section>

  <!-- envelope backs -->
  <span class="label" style="left:900px;top:403px">Envelope Back | Option 1</span>
  <section class="item back" style="left:713px;top:413px;height:140px">
    <svg class="wave" viewBox="0 0 100 100" preserveAspectRatio="none">
      <path d="M0,0 L50,40 L100,0Z" fill="#f1f3f4" stroke="#d5d8da" stroke-width=".4"/>
    </svg>
    <div class="brand" style="left:232px;top:6px;font-size:7px"><i class="mark" style="width:6px;height:6px"></i></div>
  </section>

  <span class="label" style="left:920px;top:459px">Envelope Back | Option 2</span>
  <section class="item back" style="left:756px;top:469px;width:437px;height:130px">
    <svg class="wave" viewBox="0 0 100 100" preserveAspectRatio="none">
      <path d="M0,0 L50,38 L100,0Z" fill="var(--blue)"/>
      <path d="M0,0 L50,30 L100,0Z" fill="var(--navy)"/>
    </svg>
    <div class="brand" style="left:214px;top:8px"><i class="mark" style="width:6px;height:6px;background:#fff"></i></div>
  </section>

  <span class="label" style="left:940px;top:524px">Envelope Back | Option 3</span>
  <section class="item back" style="left:804px;top:534px;width:389px;height:186px">
    <svg class="wave" viewBox="0 0 100 100" preserveAspectRatio="none">
      <path d="M0,0 L50,30 L100,0Z" fill="var(--green)"/>
      <path d="M0,0 L50,22 L100,0Z" fill="var(--lime)"/>
    </svg>
    <div class="brand" style="left:190px;top:8px"><i class="mark" style="width:6px;height:6px;background:#fff"></i></div>
  </section>

  <!-- letterheads -->
  <span class="label" style="left:170px;top:243px">Letterhead</span>
  <section class="item letterhead" style="left:31px;top:252px">
    <svg class="wave" viewBox="0 0 100 100" preserveAspectRatio="none">
      <path d="M0,100 C35,84 70,90 100,70 L100,100Z" fill="var(--green)"/>
      <path d="M0,100 C40,89 72,93 100,77 L100,100Z" fill="var(--paper)"/>
      <path d="M0,100 C45,92 75,96 100,82 L100,100Z" fill="var(--blue)"/>
    </svg>
    <div class="brand"><i class="mark"></i>Dormly Nest</div>
    <div class="contact" style="left:230px;top:26px">T 0113 496 0321<br>M 07700 900123<br>Rafik@dormlynest.co.uk<br>www.dormlynest.co.uk</div>
  </section>

  <span class="label" style="left:505px;top:243px">Letterhead</span>
  <section class="item letterhead" style="left:372px;top:252px">
    <svg class="wave" viewBox="0 0 100 100" preserveAspectRatio="none">
      <path d="M100,18 C92,45 92,75 100,92Z" fill="var(--green)"/>
      <path d="M100,30 C95,55 95,75 100,88Z" fill="var(--blue)"/>
      <path d="M40,100 C70,96 90,94 100,86 L100,100Z" fill="var(--green)"/>
    </svg>
    <div class="brand"><i class="mark"></i>Dormly Nest</div>
    <div class="contact" style="left:230px;top:26px">T 0113 496 0321<br>M 07700 900123<br>Rafik@dormlynest.co.uk<br>www.dormlynest.co.uk</div>
    <p class="footer-line">Dormly Nest Ltd · 12 Park Row, Leeds LS1 5HD · www.dormlynest.co.uk</p>
  </section>

</main>
</body>
</html>
```